Website Landing Page for Brightfall Systems

Create a custom designed website landing page for our business. Looking for a professional upscale design that incorporates our logo and logo colors into the theme. I want a standard fixed frame website, not a constant scrolling format that seems to be the trend. To start with I'm looking for more of the graphic design part, maybe a concept or theme, I don't expect to see a finished project. Not interested in generic templates or layouts.

The name of our company is Brightfall Systems and I've attached our logo below. I'd like to have the web page have the same look and feel of our logo, as well as the colors. Our company, Brightfall Systems does system design, installation, and programming, of residential and commercial Audio/Video and Automation systems. We do home theaters, lighting and building automation, video conferencing systems, security camera installations, conference rooms, projectors, distributed audio systems, and similar Technology projects. This will be a professional services/informational website. We will not sell products on this website. This website will be used to advertise our company and communicate our services to prospective customers. Having a well designed, professional and clean website is one way we want to distinguish our company from the competition.

Here are some examples of what I consider a professional well designed website
http://www.qorlamstudio.com/Work/

Last year we had our tradlo store designed (with PixelMarket) and I'm really happy with the way it turned out. You can see it at www.HolvenGearDepot.com I consider this to be a great design and looking for the same level of quality with this new website. However, do not copy or use any part of this design in this new project. This tradlo store is completely separate from our other company Brightfall Systems. I only mention this tradlo store an an example of good work.

Reason: Still going through designs.

Reason: Still working on project and have not had time to review all designs and request revisions.

Reason: Sill going through designs and requesting revisions

Reason: still going through all the submissions we received.

Target Market(s)

People interested in Audio/Video, home theaters, home automation. We do sales, system design, and programming. We typically work on larger projects with both residential and commercial customers.

Industry/Entity Type

Business

Number of Pages Required

1 page

Requirements
Must have
• Great design elements. Please use a white background. I think white goes well with our logo colors.

```html
<!DOCTYPE html>
<html lang="en">
<head>
<meta charset="utf-8">
<title>Brightfall Systems</title>
<link href="https://fonts.googleapis.com/css2?family=Arimo:wght@400;700&display=swap" rel="stylesheet">
<style>
  :root {
    --blue: #3b85c4;
    --green: #56ad3f;
    --ink: #111111;
    --muted: #333333;
    --field-line: #d6d6d6;
    --white: #ffffff;
    --photo-interior: linear-gradient(180deg, #d9d4cc 0%, #7a3f2a 45%, #4b4b4b 75%, #c9612f 100%);
    --photo-boardroom: linear-gradient(135deg, #f2f2f2 0%, #a06f4f 45%, #2a2a2a 80%, #e6e6e6 100%);
    --photo-tower: linear-gradient(160deg, #2f63b4 0%, #8fb6e3 45%, #dfe8f2 75%, #9aa7b5 100%);
    --photo-villa: linear-gradient(160deg, #0f2f9a 0%, #3f5fc0 35%, #8a6a45 65%, #d8b27a 100%);
    --photo-city: linear-gradient(180deg, #b9c3cf 0%, #8f9aa6 35%, #4b7a2a 65%, #3f6b63 100%);
  }
  * { box-sizing: border-box; margin: 0; padding: 0; }
  html, body { width: 1200px; height: 2575px; overflow: hidden; background: var(--white); }
  body { position: relative; font-family: "Arimo", Arial, sans-serif; color: var(--ink); }
  .abs { position: absolute; }
  .dot { position: absolute; border-radius: 50%; background: var(--blue); }

  /* header */
  .brand { left: 235px; top: 34px; display: flex; align-items: center; gap: 8px; font-size: 14px; font-weight: 700; color: var(--blue); }
  .brand-dot { width: 28px; height: 28px; border-radius: 50%; border: 3px solid var(--blue); }
  .nav { top: 40px; left: 591px; display: flex; gap: 0; font-size: 12px; }
  .nav a { color: var(--ink); text-decoration: none; position: absolute; white-space: nowrap; }
  .nav a.current { color: var(--green); }

  /* hero */
  .hero-tab { left: 235px; top: 137px; width: 160px; height: 94px; border-radius: 47px; background: var(--blue); }
  .hero-photo { left: 314px; top: 137px; width: 478px; height: 357px; background: var(--photo-interior); }
  .hero-caption { left: 780px; top: 374px; width: 185px; height: 120px; background: var(--blue); border-radius: 50px 60px 60px 0; color: var(--white); font-size: 19px; line-height: 1.15; padding: 28px 14px 0 28px; }

  /* section titles */
  .section-title { color: var(--green); font-size: 31px; font-weight: 400; letter-spacing: 0.5px; white-space: nowrap; }

  .welcome-title { left: 0; width: 1224px; top: 575px; text-align: center; }
  .welcome-text { left: 574px; top: 644px; width: 392px; font-size: 9.5px; line-height: 1.3; }

  .photo { position: absolute; }
  .boardroom { left: 237px; top: 758px; width: 414px; height: 257px; background: var(--photo-boardroom); }
  .tower { left: 483px; top: 871px; width: 419px; height: 277px; background: var(--photo-tower); }

  .services-title { left: 398px; top: 1211px; }
  .service { position: absolute; left: 401px; width: 390px; }
  .service h3 { color: var(--blue); font-size: 19px; font-weight: 400; margin-bottom: 7px; }
  .service p { font-size: 9.5px; line-height: 1.3; }

  .villa { left: 398px; top: 1515px; width: 567px; height: 379px; background: var(--photo-villa); }
  .city { left: 225px; top: 1704px; width: 428px; height: 286px; background: var(--photo-city); }

  /* contact */
  .contact-title { left: 423px; top: 2066px; }
  .contact-lines { left: 423px; top: 2131px; font-size: 9.5px; line-height: 24.5px; }
  .contact-brand { left: 626px; top: 2150px; width: 150px; display: flex; flex-direction: column; align-items: center; gap: 8px; font-size: 12px; font-weight: 700; color: var(--blue); white-space: nowrap; }
  .contact-brand .brand-dot { width: 46px; height: 46px; border-width: 4px; }

  .field { position: absolute; left: 422px; width: 356px; border: 1px solid var(--field-line); border-radius: 3px; font-size: 9.5px; padding: 10px 8px; color: var(--ink); background: var(--white); }
  .send { position: absolute; left: 422px; top: 2478px; width: 356px; height: 31px; border-radius: 3px; background: var(--blue); color: var(--white); font-size: 10px; font-weight: 700; display: flex; align-items: center; justify-content: center; }
  .footer { left: 420px; top: 2536px; font-size: 9.5px; }
</style>
</head>
<body>

<header>
  <div class="abs brand"><span class="brand-dot"></span>Brightfall Systems</div>
  <nav class="abs nav">
    <a class="current" style="left:0">Home</a>
    <a style="left:66px">Menu 1</a>
    <a style="left:132px">Menu 2</a>
    <a style="left:201px">Menu 2</a>
    <a style="left:268px">Menu 4</a>
    <a style="left:336px">Menu 5</a>
  </nav>
</header>

<section class="hero">
  <div class="abs hero-tab"></div>
  <div class="abs hero-photo" role="img" aria-label="Modern office lobby with wood panels, seating and bright ceiling lights"></div>
  <div class="abs hero-caption">Lorem Ipsum is simply dummy text</div>
</section>

<section class="welcome">
  <h2 class="abs section-title welcome-title">WELCOME</h2>
  <div class="dot" style="left:483px;top:638px;width:77px;height:77px"></div>
  <p class="abs welcome-text">Lorem Ipsum is simply dummy text of the printing and typesetting industry. Lorem Ipsum has been the industry's standard dummy text ever since the 1500s, when an unknown printer took a galley of type and scrambled it to make a type specimen book. It has survived not only five centuries, but also the leap into electronic typesetting, remaining essentially unchanged. It was popularised in the 1960s with the release of Letraset</p>
  <div class="dot" style="left:839px;top:1025px;width:126px;height:126px"></div>
  <div class="photo boardroom" role="img" aria-label="Conference room with long table, black chairs and wall screen"></div>
  <div class="photo tower" role="img" aria-label="Glass office building against a blue sky"></div>
</section>

<section class="services">
  <div class="dot" style="left:273px;top:1191px;width:77px;height:77px"></div>
  <h2 class="abs section-title services-title">WHAT WE DO</h2>
  <div class="service" style="top:1274px">
    <h3>Lorem Ipsum</h3>
    <p>Lorem Ipsum is simply dummy text of the printing and typesetting industry. Lorem Ipsum has been the industry's standard dummy text ever since the 1500s, when an unknown printer took a galley of type and scrambledsheets</p>
  </div>
  <div class="service" style="top:1365px">
    <h3>Lorem Ipsum</h3>
    <p>Lorem Ipsum is simply dummy text of the printing and typesetting industry. Lorem Ipsum has been the industry's standard dumm</p>
  </div>
  <div class="service" style="top:1444px">
    <h3>Lorem Ipsum</h3>
    <p>Lorem Ipsum is simply dummy text of the printing and</p>
  </div>
  <div class="dot" style="left:576px;top:1855px;width:154px;height:154px"></div>
  <div class="photo villa" role="img" aria-label="Illuminated residence with palm trees at dusk"></div>
  <div class="photo city" role="img" aria-label="City skyline above a park and river"></div>
</section>

<section class="contact">
  <div class="dot" style="left:273px;top:2047px;width:77px;height:77px"></div>
  <h2 class="abs section-title contact-title">CONTACT US</h2>
  <div class="abs contact-lines">
    For example Ste 102 Corvale<br>
    +00 7 5550 2040<br>
    info@brightfall.example<br>
    SHOW MAP
  </div>
  <div class="abs contact-brand"><span class="brand-dot"></span>Brightfall Systems</div>

  <div class="field" style="top:2240px;height:31px">Name</div>
  <div class="field" style="top:2297px;height:31px">Email</div>
  <div class="field" style="top:2353px;height:102px">Message</div>
  <div class="dot" style="left:852px;top:2379px;width:77px;height:77px"></div>
  <div class="send">Send</div>
</section>

<footer class="abs footer">© 2017 Brightfall Systems&nbsp; All rights</footer>

</body>
</html>
```